VeloNest Crowdfunding Website 1st Page

I am looking to have a first page created for a new crowd funding website that knocks down the biggest hurdle that creative types and start ups face, legal costs. For creative projects and innovative products, we are providing intellectual property and certain other legal services wrapped into the project costs.

I am using a white label crowdfunding platform that that has a standard look and feel of most crowdfunding sites e.g. tiles with campaigns, listing of campaigns categories, create new campaign options, and donate to campaigns etc. The white label program is branded with the VeloNest logo and colors. At present there is a front page that is just a place holder for someone at ArtHive's great design! What I need is an eye-catching first page that visually and through content optimizes the VeloNest brand. (There should be space for content for those looking to raise money and those looking to donate to campaigns.)

www.pledgewave.example is, of course, the reigning King of crowdfunding. They have been so successful that they no longer have to entice people to launch campaigns there. (So they don't speak as much to those looking to raise money.) Unlike Pledgewave, of the challenges is that I have two customers I need to engage. The first is the potential crowdfund campaign owner who is looking to raise money. The second customer is the donor.

I am looking for a smart page from a marketing standpoint that also grabs you. One should feel the energy of "the crowd" when they look at the page.

Some information regarding the logo: The font is Kabel BK BT. The primary blue is R33, G121, B 159. Hex21799F and the primary greenis R179, G210, B54 Hex B3D236. The third file is a slight variation on the VN logo that you are free to use as well. (Unfortunately, I don't have all the color information for that one readily available.) If you need more files, please just let me know.

Industry/Entity Type

Marketing

Font styles to use
Other font styles liked:
• Kabel Bk BT or complimentary

Requirements
Must have
• Please use the slogan "Where the crowd meets great ideas".

```html
<!DOCTYPE html>
<html lang="en">
<head>
<meta charset="utf-8">
<title>VeloNest — Where the Crowd Meets Great Ideas</title>
<link href="https://fonts.googleapis.com/css2?family=Roboto:wght@300;400;500;700&display=swap" rel="stylesheet">
<style>
:root{
  --brand-blue:#21799F;
  --sky-blue:#3da4d9;
  --brand-green:#B3D236;
  --cta-green:#a5c93a;
  --orange:#f29a2e;
  --ink:#333;
  --muted:#777;
  --line:#dcdcdc;
  --paper:#fff;
  --night:#0b0b0b;
  --footer:#2b2b2b;
  --footer-deep:#1f1f1f;
  --band:#e9e9e9;
}
*{box-sizing:border-box;margin:0;padding:0}
html,body{width:1200px;height:2704px;overflow:hidden;background:var(--paper)}
body{font-family:'Roboto',Arial,sans-serif;color:var(--ink);position:relative}
.page{position:relative;width:1200px;height:2704px;overflow:hidden}
.abs{position:absolute}

/* top bar */
.topbar{left:0;top:0;width:1200px;height:48px;background:var(--paper);border-bottom:1px solid var(--line)}
.tab{top:0;height:48px;width:52px;color:#fff;font-size:8px;font-weight:700;line-height:1.1;padding:18px 6px 0;text-transform:uppercase}
.tab-start{left:0;background:var(--cta-green)}
.tab-donate{left:52px;background:var(--sky-blue)}
.brand{left:458px;top:10px;display:flex;align-items:center;gap:8px;font-size:22px;font-weight:400;color:var(--brand-blue)}
.brand .dot{width:24px;height:24px;border-radius:50%;background:var(--brand-green)}
.nav{right:20px;top:16px;display:flex;gap:18px;align-items:center;font-size:10px;font-weight:700;color:var(--ink)}
.nav .login{border:1px solid var(--ink);padding:3px 10px;border-radius:2px}

/* hero */
.hero{left:0;top:48px;width:1200px;height:640px;background:var(--night)}
.hero-photo{left:0;top:0;width:1200px;height:320px;background:linear-gradient(180deg,#9ea3a6 0%,#6d7275 45%,#2a2c2d 85%,#0b0b0b 100%)}
.hero-title{left:0;top:340px;width:1200px;text-align:center;font-size:40px;font-weight:300;color:var(--brand-green)}
.hero-copy{left:300px;top:396px;width:600px;text-align:center;color:#e6e6e6;font-size:11.5px;line-height:1.55}
.btn{display:inline-block;color:#fff;font-size:13px;font-weight:700;text-transform:uppercase;text-align:center;border-radius:2px}
.hero-start{left:360px;top:496px;width:214px;height:46px;line-height:46px;background:var(--cta-green)}
.hero-donate{left:596px;top:496px;width:214px;height:46px;line-height:46px;background:var(--sky-blue)}
.hero-edge{left:0;top:684px;width:1200px;height:4px;background:var(--brand-green)}

/* sections */
.section-title{left:0;width:1200px;text-align:center;font-size:40px;font-weight:300;color:#3a3a3a}
.rule{left:150px;width:900px;height:1px;background:var(--line)}
.view-all{font-size:9px;font-weight:700;border:1px solid #555;padding:3px 7px;border-radius:2px;color:var(--ink);line-height:1.2}
.filters{left:150px;top:818px;display:flex;gap:22px;font-size:10px;font-weight:500;color:var(--muted);text-transform:uppercase;line-height:1.2}
.filters .active{color:var(--ink);font-weight:700;border-bottom:2px solid var(--ink);padding-bottom:7px}

.card{top:858px;width:212px;height:560px;border:1px solid var(--line);background:#fff}
.card-cat{height:22px;line-height:22px;text-align:center;font-size:8px;font-weight:700;color:var(--ink);text-transform:uppercase}
.card-img{height:170px;margin:0 6px}
.card-body{padding:10px 10px 0}
.card-title{color:var(--cta-green);font-size:12px;font-weight:700;line-height:1.3;margin-bottom:8px}
.card-text{font-size:9.5px;line-height:1.5;color:var(--muted);height:72px}
.card-goal{text-align:center;font-size:10px;margin-top:14px}
.card-goal b{color:#d9534f;font-size:11px}
.card-days{text-align:center;font-size:10px;color:var(--muted);margin-top:4px}
.card-days b{color:var(--sky-blue)}
.bar{height:10px;border:1px solid #ccc;margin:16px 0 8px;background:#f3f3f3}
.bar span{display:block;height:100%;background:var(--orange)}
.card-share{text-align:right;font-size:9px;color:var(--muted)}
.card-btn{position:absolute;left:10px;right:10px;bottom:12px;height:26px;line-height:26px;background:var(--sky-blue);font-size:9px}

/* success */
.story-img{left:150px;top:1598px;width:440px;height:290px;background:linear-gradient(135deg,#d9d2c6 0%,#c8a16b 45%,#8a6a42 100%)}
.story{left:620px;top:1598px;width:430px}
.story h3{color:var(--cta-green);font-size:15px;font-weight:700;line-height:1.35}
.story .raised{font-size:12px;margin-top:8px}
.story .raised b{color:#d9534f;font-size:15px}
.story .meta{font-size:10px;color:var(--muted);margin-top:4px}
.story p{font-size:10.5px;line-height:1.6;color:var(--muted);margin-top:22px}
.story .share{font-size:9px;color:var(--muted);text-align:right;margin-top:14px}
.dots{left:0;top:1905px;width:1200px;display:flex;justify-content:center;gap:6px}
.dots i{width:7px;height:7px;border-radius:50%;background:#ccc;display:block}
.dots i.on{background:#666}

/* partners */
.partners{left:150px;top:2090px;width:900px;height:96px;border:1px solid var(--line);display:flex;justify-content:space-around;align-items:center;padding:0 20px}
.badge{height:22px;border-radius:3px}

/* newsletter */
.newsletter{left:0;top:2268px;width:1200px;height:78px;background:var(--band)}
.nl-title{left:150px;top:2280px;font-size:24px;font-weight:300;color:#444;line-height:1.2}
.nl-sub{left:150px;top:2314px;font-size:9px;color:var(--muted)}
.field{top:2292px;height:26px;background:#fff;border:1px solid #ccc;font-size:9px;color:#999;padding:7px 8px;line-height:1.2}
.nl-btn{left:930px;top:2292px;width:120px;height:26px;line-height:26px;background:var(--orange);font-size:10px}

/* footer */
.footer{left:0;top:2346px;width:1200px;height:358px;background:var(--footer)}
.fcol{top:2364px;color:#ccc;font-size:9.5px;line-height:1.65}
.fcol h4{color:#fff;font-size:10px;font-weight:700;text-transform:uppercase;margin-bottom:4px;border-bottom:1px solid #444;padding-bottom:4px;width:180px}
.legal{left:150px;top:2508px;width:900px;color:#999;font-size:8px;line-height:1.6}
.legal b{color:#ddd}
.seals{left:0;top:2590px;width:1200px;display:flex;justify-content:center;gap:10px}
.seals span{width:70px;height:26px;background:#e4e4e4;border-radius:2px}
.copy{left:0;top:2652px;width:1200px;height:52px;background:var(--footer-deep);color:#888;font-size:9px;text-align:center;line-height:52px}
</style>
</head>
<body>
<div class="page">

  <header class="abs topbar">
    <a class="abs tab tab-start">Start a<br>Campaign</a>
    <a class="abs tab tab-donate">Make a<br>Donation</a>
    <div class="abs brand"><span class="dot"></span>VeloNest</div>
    <nav class="abs nav"><span>ABOUT US</span><span>HELP?</span><span class="login">LOGIN</span></nav>
  </header>

  <section class="abs hero">
    <div class="abs hero-photo" role="img" aria-label="Crowd of people silhouetted in a bright open hall"></div>
    <h1 class="abs hero-title">Where the Crowd Meets Great Ideas!</h1>
    <p class="abs hero-copy">Lorem ipsum dolor sit amet, consectetur adipiscing elit. Phasellus et elit vitae massa placerat volutpat. Quisque volutpat sem at sem euismod, vitae vulputate est venenatis. Praesent ac tellus nisi. Praesent aliquet ipsum fringilla tellus vehicula gravida. Vestibulum quis neque eu sem condimentum congue. Phasellus varius, nunc at porttitor sodales, nunc tortor vestibulum metus.</p>
    <a class="abs btn hero-start">Start a Campaign</a>
    <a class="abs btn hero-donate">Make a Donation</a>
  </section>
  <div class="abs hero-edge"></div>

  <h2 class="abs section-title" style="top:756px">Campaigns</h2>
  <div class="abs filters"><span class="active">Featured</span><span>Latest</span><span>Popular</span><span>Closing Soon</span><span>Completed</span></div>
  <span class="abs view-all" style="left:992px;top:818px">VIEW ALL</span>
  <div class="abs rule" style="top:839px"></div>

  <article class="abs card" style="left:150px">
    <div class="card-cat">Art | Los Angeles</div>
    <div class="card-img" role="img" aria-label="Colourful painted portrait artwork" style="background:linear-gradient(135deg,#3a8fd0,#d6483c 55%,#e9c24a)"></div>
    <div class="card-body">
      <div class="card-title">Lorem Ipsum Dolor Sit Amet Consectetur Adipiscing Elit</div>
      <div class="card-text">Phasellus vestibulum quam nec erat semper luctus. Aenean dapibus auctor accumsan nisl, ut ornare metus vitae lorem dictum rutrum.</div>
      <div class="card-goal"><b>25,000 / $10</b> raised</div>
      <div class="card-days"><b>8 days</b> left</div>
      <div class="bar"><span style="width:48%"></span></div>
      <div class="card-share">Share ▢ ▢ ▢</div>
    </div>
    <a class="btn card-btn">Make a Donation ›</a>
  </article>

  <article class="abs card" style="left:380px">
    <div class="card-cat">Community | Santa Ana</div>
    <div class="card-img" role="img" aria-label="Group of children in a classroom" style="background:linear-gradient(135deg,#c9a886,#7c8fa8 60%,#4c5f7a)"></div>
    <div class="card-body">
      <div class="card-title">Nunc Fringilla Magna Ut Commodo Enim Mauris</div>
      <div class="card-text">Cras viverra turpis. Sed condimentum justo dui, a sollicitudin ipsum, tincidunt at egestas lorem. Donec ornare urna, vel interdum erat.</div>
      <div class="card-goal"><b>$14,500 / $10</b> raised</div>
      <div class="card-days"><b>3 days</b> left</div>
      <div class="bar"><span style="width:70%"></span></div>
      <div class="card-share">Share ▢ ▢ ▢</div>
    </div>
    <a class="btn card-btn">Make a Donation ›</a>
  </article>

  <article class="abs card" style="left:610px">
    <div class="card-cat">Fundraisers | Sea Brook</div>
    <div class="card-img" role="img" aria-label="Smiling toddler on a light background" style="background:linear-gradient(135deg,#f2e4d6,#e0b89a 60%,#c48c6a)"></div>
    <div class="card-body">
      <div class="card-title">Fringilla Vitae Adipiscing Sem Nam Interdum Ante</div>
      <div class="card-text">Nulla facilisi. Mauris placerat urna sed diam aliquet, non pulvinar orci tempor. Integer porta lectus vitae felis sagittis venenatis.</div>
      <div class="card-goal"><b>$1,575 / $10</b> raised</div>
      <div class="card-days"><b>12 days</b> left</div>
      <div class="bar"><span style="width:30%"></span></div>
      <div class="card-share">Share ▢ ▢ ▢</div>
    </div>
    <a class="btn card-btn">Make a Donation ›</a>
  </article>

  <article class="abs card" style="left:840px">
    <div class="card-cat">Sports | Chicago</div>
    <div class="card-img" role="img" aria-label="Snowboarder jumping against a blue sky" style="background:linear-gradient(180deg,#5aa6dd,#a9d2ee 60%,#eef5fa)"></div>
    <div class="card-body">
      <div class="card-title">Aliquam Erat Volutpat Donec Convallis Facilisis Nisl</div>
      <div class="card-text">Vivamus sagittis lacus vel augue laoreet rutrum faucibus dolor auctor. Donec id elit non mi porta gravida at eget metus.</div>
      <div class="card-goal"><b>25,000 / $10</b> raised</div>
      <div class="card-days"><b>8 days</b> left</div>
      <div class="bar"><span style="width:55%"></span></div>
      <div class="card-share">Share ▢ ▢ ▢</div>
    </div>
    <a class="btn card-btn">Make a Donation ›</a>
  </article>

  <h2 class="abs section-title" style="top:1486px">Success Stories</h2>
  <span class="abs view-all" style="left:992px;top:1552px">VIEW ALL</span>
  <div class="abs rule" style="top:1573px"></div>

  <div class="abs story-img" role="img" aria-label="Three puppies sitting together"></div>
  <div class="abs story">
    <h3>Lorem Ipsum Dolor Sit Amet Consectetur Adipiscing Elit</h3>
    <div class="raised"><b>$5,000</b> funded by <b>25</b> funders</div>
    <div class="meta">Animals | Pittsburgh, PA</div>
    <p>Aenean at nisl ut nibh volutpat euismod in interdum orci. Quisque malesuada placerat erat, dignissim ultrices justo porttitor vel. Cras ut dolor leo. Integer sit amet dui, sed tincidunt dolor, sed dictum purus. Nunc elit pellentesque nunc. Suspendisse tincidunt dictum tincidunt.</p>
    <div class="share">Share ▢ ▢ ▢</div>
  </div>
  <div class="abs dots"><i class="on"></i><i></i><i></i><i></i><i></i></div>

  <h2 class="abs section-title" style="top:1978px">Our Partners</h2>
  <span class="abs view-all" style="left:992px;top:2044px">VIEW ALL</span>
  <div class="abs rule" style="top:2065px"></div>
  <div class="abs partners">
    <span class="badge" style="width:70px;background:#7fa6c9"></span>
    <span class="badge" style="width:60px;background:#2d5aa7"></span>
    <span class="badge" style="width:26px;height:26px;background:#f58220"></span>
    <span class="badge" style="width:80px;background:#9a9a9a"></span>
    <span class="badge" style="width:60px;background:#c8242f"></span>
    <span class="badge" style="width:70px;background:#2f62a8"></span>
    <span class="badge" style="width:80px;background:#9cc26a"></span>
  </div>

  <div class="abs newsletter"></div>
  <div class="abs nl-title">Newsletter Sign Up</div>
  <div class="abs nl-sub">Get project news and updates sent to your inbox</div>
  <div class="abs field" style="left:560px;width:170px">Name</div>
  <div class="abs field" style="left:740px;width:180px">Email</div>
  <a class="abs btn nl-btn">Subscribe ›</a>

  <footer class="abs footer"></footer>
  <div class="abs fcol" style="left:150px"><h4>Information</h4>About Us<br>How It Works<br>Partners<br>Blog<br>Press</div>
  <div class="abs fcol" style="left:380px"><h4>Support &amp; Legal</h4>FAQs<br>Contact Us<br>Site Map<br>Terms of Use<br>Privacy Policy</div>
  <div class="abs fcol" style="left:610px"><h4>Account</h4>Login<br>Register<br>Forgot Password?</div>
  <div class="abs fcol" style="left:840px"><h4>Get in Touch</h4>1200 Harbor Ave<br>Los Angeles, CA 90012<br>(555) 014-2290<br>hello@velonest.example</div>
  <p class="abs legal"><b>TERMS AND CONDITIONS:</b> Lorem ipsum dolor sit amet, consectetur adipiscing elit. Donec sed ante vitae turpis. Nam condimentum ligula nec ante dignissim, vel dignissim nisl facilisis. Morbi in lacus at mauris luctus faucibus. Curabitur vel metus tincidunt, gravida nunc sed, elementum erat. Integer ac velit non risus tempor posuere. Mauris ullamcorper lacus ut nibh feugiat, ut congue arcu dapibus. Praesent tincidunt velit quis odio volutpat, in dictum nunc tempus. Pellentesque habitant morbi tristique senectus et netus et malesuada fames ac turpis egestas. Sed vitae magna vitae turpis porta commodo. Vestibulum ante ipsum primis in faucibus orci luctus et ultrices posuere cubilia curae.</p>
  <div class="abs seals"><span></span><span></span><span></span></div>
  <div class="abs copy">© 2014 VeloNest Crowdfunding. All Rights Reserved.</div>

</div>
</body>
</html>
```